依頼詳細
集合場所が分かりにくいので、周辺が混みあうときには2~3本立てて、その目印に使います。なるべく目立つ印象で、明るく楽しい感じが伝わってくるものが良いです。写真も添付しますのでご利用ください。
記載項目
記載項目:鳥取砂丘でパラグライダー体験!
サイズ:一般的なのぼりのサイズ(600×1800ミリ)
希望イメージ
シンプル 複雑
単色 カラフル
暗い 明るい
日常 高級
遊び心 厳粛
未来的 伝統的
女性的 男性的
希望する色
青、黄、オレンジ
納品ファイル
• 高解像度JPG (.jpg)
• イラストレーター形式 (.ai)
補足説明
当方のHPは、
http://hane.kumoba.info/
になります。
画像等は、参考にしていただければと思います。
■ 選んだ理由

今回かなり悩みました。
期間をじっくり置いて、いろいろな視点ですべての作品を見させていただいた中で、写真を大きくはっきり使っていただいたのと、その配置が絶妙で、文字の自由度が大きくなる点を評価しました。
写真の切り取り方が良かったと思います。

■ 提案者全員のお礼・コメント

多数のご提案まことにありがとうございました。
甲乙つけがたいものが多くて、自分がどうこう評価するにはおこがましい感覚を受けながらも、みなさまの作品をじっくり拝見して、吟味させていただきました。
写真以外の可能性も感じたり、キャラや文字を面白くデフォルメしてくださったり、斬新な構図を見せてくださったり、う~んと感心ばかりしていました。
当方、まったくデザインに関して素人にも関わらず、いろいろなことを勉強させていただいたように思います。
皆さまの貴重な時間を、このたびは本当にありがとうございました。m(_ _)m

```html
<!DOCTYPE html>
<html lang="ja">
<head>
<meta charset="utf-8">
<title>鳥取砂丘 パラグライダー のぼり</title>
<link rel="stylesheet" href="https://fonts.googleapis.com/css2?family=Noto+Sans+JP:wght@900&display=swap">
<style>
  :root {
    --sky-deep: #1f7fd6;
    --sky-mid: #5fb4ee;
    --sky-light: #cfe8fb;
    --cloud: #f4f8fc;
    --sand: #d9c196;
    --sea: #3d86c4;
    --band-blue: #1a8fe3;
    --title-yellow: #fff100;
    --title-blue: #0d5fc0;
    --accent-red: #e60012;
    --place-navy: #13326e;
    --white: #ffffff;
  }
  * { margin: 0; padding: 0; box-sizing: border-box; }
  html, body { width: 1200px; height: 3604px; overflow: hidden; background: var(--white); }
  .banner {
    position: relative;
    width: 1200px;
    height: 3604px;
    overflow: hidden;
    font-family: "Noto Sans JP", sans-serif;
    font-weight: 900;
  }
  .sky-photo {
    position: absolute;
    left: 0; top: 0;
    width: 1200px; height: 3240px;
    background:
      radial-gradient(ellipse 900px 500px at 420px 2750px, var(--cloud) 0%, rgba(244,248,252,0) 70%),
      radial-gradient(ellipse 700px 260px at 700px 1250px, rgba(244,248,252,0.85) 0%, rgba(244,248,252,0) 70%),
      linear-gradient(180deg, var(--sky-deep) 0%, var(--sky-mid) 30%, var(--sky-light) 48%, var(--sky-mid) 62%, var(--sky-deep) 78%, var(--sky-light) 88%, var(--sea) 92%, var(--sand) 96%, var(--sand) 100%);
  }
  .vtext {
    position: absolute;
    writing-mode: vertical-rl;
    text-orientation: upright;
    line-height: 1;
    paint-order: stroke fill;
    white-space: nowrap;
  }
  .main-title {
    left: 40px; top: 290px;
    font-size: 400px;
    letter-spacing: -20px;
    color: var(--title-yellow);
    -webkit-text-stroke: 34px var(--title-blue);
    transform: scaleX(1.35) rotate(-2deg);
    transform-origin: left top;
  }
  .same-day {
    left: 910px; top: 270px;
    font-size: 245px;
    letter-spacing: 2px;
    color: var(--accent-red);
    -webkit-text-stroke: 26px var(--white);
  }
  .place {
    left: 670px; top: 1060px;
    font-size: 175px;
    letter-spacing: -8px;
    color: var(--place-navy);
    -webkit-text-stroke: 22px var(--white);
  }
  .shop-band {
    position: absolute;
    left: 0; top: 3240px;
    width: 1200px; height: 364px;
    background: var(--band-blue);
    color: var(--title-yellow);
    text-align: center;
  }
  .shop-name {
    font-size: 190px;
    line-height: 1;
    letter-spacing: 60px;
    margin-left: 60px;
    padding-top: 4px;
  }
  .shop-phone {
    display: flex;
    align-items: center;
    justify-content: center;
    gap: 12px;
    font-size: 138px;
    line-height: 1;
    margin-top: 22px;
  }
  .shop-phone svg { width: 110px; height: 110px; fill: var(--title-yellow); }
</style>
</head>
<body>
  <div class="banner">
    <div class="sky-photo" role="img" aria-label="鳥取砂丘の青空を飛ぶ色とりどりのパラグライダーと、雲、海、砂丘の写真"></div>

    <div class="vtext place">鳥取砂丘</div>
    <div class="vtext main-title">パラグライダー</div>
    <div class="vtext same-day">当日参加できます！</div>

    <div class="shop-band">
      <p class="shop-name">空丘本舗</p>
      <p class="shop-phone">
        <svg viewBox="0 0 100 100" aria-hidden="true">
          <path d="M10 30 Q50 5 90 30 L80 45 Q70 38 68 28 Q50 22 32 28 Q30 38 20 45 Z"/>
          <path d="M30 42 H70 L88 88 H12 Z M50 52 A14 14 0 1 0 50.1 52 Z" fill-rule="evenodd"/>
        </svg>
        <span>0857-11-2233</span>
      </p>
    </div>
  </div>
</body>
</html>
```